Las Vegas Themed Video & Messaging Zelpad App

We have designed an Zelpad app that allows people to share videos and message one another while visiting Las Vegas, Nevada. However, without a simple, compelling design this app will be "just like the rest". This is where you come in.

As a version 1.0 of this app, we want to test the market as inexpensively as possible. There are other screens that we will need to be designed; during development we will be coming back to you for further iterations and enhancements. Consider this contest a paid interview, in other words.

This app will be available to users in the Quorvo Apps Mart. A mockup is attached to the Files section of this brief.

Our mockup is intentionally devoid of almost all styling because we did not want to get in front of your design. The attached mockup exists only to give you a general guide towards the "feel" of the app, but the elements themselves and their placements can (and should) be freely changed by you.

Please be creative; we're excited to see your work!

Requirements
Must have
• Simplicity is the focus. We'd like to see only a few screens from you to judge your work:

• The home screen.
• The messaging screen.
• A screen that records a video.

Nice to have
• A clean, contemporary design:

• Beautiful typography.
• A "flat-ish" design, avoiding skeuomorphism.

```html
<!DOCTYPE html>
<html lang="en">
<head>
<meta charset="utf-8">
<title>Chat – Uncle Bob</title>
<link href="https://fonts.googleapis.com/css2?family=Open+Sans:wght@400;600&family=Kaushan+Script&family=Arimo:wght@400;700&display=swap" rel="stylesheet">
<style>
  :root{
    --bg:#3b3b3b;
    --header:#1d1d1d;
    --accent:#f4a100;
    --red:#e8141b;
    --bubble-in:#454545;
    --bubble-out:#1b1b1b;
    --bubble-text:#d9d9d9;
    --composer:#333333;
    --field:#b9b9b9;
    --ink:#0a0a0a;
    --kb-top:#8b93a0;
    --kb-bottom:#5a6270;
    --key:#f7f7f7;
    --key-shade:#d6d6d8;
    --key-dark:#6f7785;
    --key-dark-2:#5a6170;
    --shift-top:#e9ecf2;
    --shift-bottom:#b9c0cc;
  }
  *{box-sizing:border-box;margin:0;padding:0}
  html,body{width:676px;height:1200px;overflow:hidden;background:var(--bg)}
  .screen{position:absolute;left:0;top:0;width:640px;height:1136px;transform:scale(1.05625);transform-origin:0 0;background:var(--bg);overflow:hidden;font-family:"Open Sans",sans-serif}
  .app-bar{position:absolute;left:0;top:0;width:640px;height:100px;background:var(--header);box-shadow:0 4px 8px rgba(0,0,0,.45);z-index:2}
  .back-button{position:absolute;left:10px;top:18px;width:116px;height:65px}
  .back-button span{position:absolute;left:22px;top:0;width:94px;height:65px;line-height:64px;text-align:center;color:#fff;font:600 38px "Open Sans",sans-serif}
  .contact-name{position:absolute;left:0;right:0;top:10px;text-align:center;color:var(--accent);font-family:"Kaushan Script",cursive;font-weight:400;font-size:50px;line-height:80px;letter-spacing:1px}
  .add-button{position:absolute;left:560px;top:26px;width:50px;height:50px}
  .message{position:absolute;height:90px;line-height:88px;font-size:46px;color:var(--bubble-text);white-space:nowrap;letter-spacing:-1px}
  .message--incoming{left:0;top:112px;width:613px;background:var(--bubble-in);padding-left:16px}
  .message--outgoing{left:26px;top:226px;width:614px;background:var(--bubble-out);padding-left:14px}
  .composer{position:absolute;left:0;top:617px;width:640px;height:88px;background:var(--composer)}
  .composer-field{position:absolute;left:14px;top:10px;width:448px;height:65px;border-radius:16px;background:var(--field);padding-left:18px;line-height:64px;font-size:44px;color:var(--ink);letter-spacing:-1.5px}
  .send-button{position:absolute;left:481px;top:9px;width:147px;height:67px;border-radius:16px;background:var(--accent);text-align:center;line-height:66px;font-size:44px;color:#eee}
  .keyboard{position:absolute;left:0;top:705px;width:640px;height:431px;background:linear-gradient(var(--kb-top),var(--kb-bottom))}
  .key-row{position:absolute;display:flex;gap:12px}
  .key{flex:none;width:52px;height:78px;border-radius:8px;background:linear-gradient(var(--key),var(--key-shade));box-shadow:0 2px 0 rgba(0,0,0,.45);display:flex;align-items:center;justify-content:center;font:700 40px "Arimo",sans-serif;color:#111}
  .key--dark{background:linear-gradient(var(--key-dark),var(--key-dark-2));color:#fff}
  .key--shift{width:72px;margin-right:12px;background:linear-gradient(var(--shift-top),var(--shift-bottom))}
  .key--delete{width:72px;margin-left:12px}
  .key--fn{width:68px;font-size:30px;font-weight:400}
  .key--space{width:308px;font-size:30px;font-weight:400;color:#444}
  .key--return{width:148px;font-size:30px;font-weight:400}
  .row-1{left:6px;top:22px}
  .row-2{left:38px;top:130px}
  .row-3{left:6px;top:238px}
  .row-4{left:6px;top:347px}
</style>
</head>
<body>
<main class="screen">
  <header class="app-bar">
    <a class="back-button" aria-label="Back">
      <svg width="116" height="65" viewBox="0 0 116 65"><path d="M30 0H108a8 8 0 0 1 8 8V57a8 8 0 0 1-8 8H30L0 32.5Z" fill="var(--red)"/></svg>
      <span>Back</span>
    </a>
    <h1 class="contact-name">Uncle Bob</h1>
    <svg class="add-button" viewBox="0 0 50 50" aria-label="Add"><rect x="20" y="2" width="10" height="46" fill="var(--red)"/><rect x="2" y="20" width="46" height="10" fill="var(--red)"/></svg>
  </header>

  <p class="message message--incoming">Did you see the last video?</p>
  <p class="message message--outgoing">I’ll watch it now.</p>

  <div class="composer">
    <div class="composer-field">Great video!</div>
    <div class="send-button">Send</div>
  </div>

  <div class="keyboard">
    <div class="key-row row-1">
      <div class="key">Q</div><div class="key">W</div><div class="key">E</div><div class="key">R</div><div class="key">T</div><div class="key">Y</div><div class="key">U</div><div class="key">I</div><div class="key">O</div><div class="key">P</div>
    </div>
    <div class="key-row row-2">
      <div class="key">A</div><div class="key">S</div><div class="key">D</div><div class="key">F</div><div class="key">G</div><div class="key">H</div><div class="key">J</div><div class="key">K</div><div class="key">L</div>
    </div>
    <div class="key-row row-3">
      <div class="key key--shift" aria-label="Shift">
        <svg width="40" height="36" viewBox="0 0 40 36"><path d="M20 2L38 20H28V34H12V20H2Z" fill="#fff" stroke="#8a909a" stroke-width="1.5"/></svg>
      </div>
      <div class="key">Z</div><div class="key">X</div><div class="key">C</div><div class="key">V</div><div class="key">B</div><div class="key">N</div><div class="key">M</div>
      <div class="key key--delete key--dark" aria-label="Delete">
        <svg width="48" height="32" viewBox="0 0 48 32"><path d="M14 2H44a2 2 0 0 1 2 2V28a2 2 0 0 1-2 2H14L2 16Z" fill="#fff"/><path d="M22 9L36 23M36 9L22 23" stroke="#5f6674" stroke-width="4.5" stroke-linecap="round"/></svg>
      </div>
    </div>
    <div class="key-row row-4">
      <div class="key key--fn key--dark">123</div>
      <div class="key key--fn key--dark" aria-label="Dictation">
        <svg width="22" height="40" viewBox="0 0 22 40"><rect x="6" y="2" width="10" height="22" rx="5" fill="#fff"/><path d="M2 18a9 9 0 0 0 18 0M11 27V36M5 37H17" stroke="#fff" stroke-width="2.5" fill="none"/></svg>
      </div>
      <div class="key key--space">space</div>
      <div class="key key--return key--dark">return</div>
    </div>
  </div>
</main>
</body>
</html>
```